Brasko Construction Business Card

I need a business card design for my company.
We are a construction/machinery company.
I would like to see my logo on the front of the card and my details on the other side
I would like the card to be black or dark grey in colour,with my logo as i send it or modified with a lighter blue colour
I would like to see the design kept fairly simple,but eye catching at the same time
Industry/Entity Type
Business
Contact Information for Business Card
Name
Phone Number
Address
Email
Colors
00a990
1b1b1b
000000
474747
ececec

```html
<!DOCTYPE html>
<html lang="en">
<head>
<meta charset="utf-8">
<title>Brasko Construction Business Card</title>
<link rel="stylesheet" href="https://fonts.googleapis.com/css2?family=Arimo:wght@400;700&display=swap">
<style>
  :root {
    --backdrop: #d9d9d9;
    --card: #262626;
    --logo-ink: #141414;
    --accent: #2aa3df;
    --text: #ffffff;
  }
  * { margin: 0; padding: 0; box-sizing: border-box; }
  html, body {
    width: 1200px; height: 1000px; overflow: hidden;
    background: var(--backdrop);
    font-family: "Arimo", Arial, sans-serif;
  }
  .canvas { position: relative; width: 1200px; height: 1000px; }
  .card {
    position: absolute; left: 265px; width: 666px; height: 397px;
    background: var(--card);
  }
  .card-front { top: 73px; }
  .card-back { top: 532px; }

  .brand {
    position: absolute; left: 0; right: 0; top: 170px;
    text-align: center;
    color: var(--logo-ink);
    font-weight: 700;
    font-size: 44px;
    letter-spacing: 3px;
    text-transform: uppercase;
    line-height: 1.1;
  }

  .identity {
    position: absolute; right: 362px; top: 172px;
    text-align: right;
  }
  .person-name {
    color: var(--accent); font-weight: 700; font-size: 22px; line-height: 26px;
  }
  .person-role {
    color: var(--text); font-size: 16px; line-height: 22px; margin-top: 2px;
  }
  .divider {
    position: absolute; left: 328px; top: 168px;
    width: 2px; height: 60px; background: var(--text);
  }
  .contact-list {
    position: absolute; left: 352px; top: 164px; list-style: none;
  }
  .contact-list li {
    display: flex; align-items: center; gap: 10px;
    color: var(--text); font-size: 16px; line-height: 23px;
  }
  .contact-list svg { width: 15px; height: 15px; fill: var(--accent); flex: none; }
  .address {
    position: absolute; left: 0; right: 0; top: 337px;
    display: flex; justify-content: center; align-items: center; gap: 8px;
    color: var(--text); font-size: 16px; letter-spacing: 0.4px;
  }
  .address svg { width: 14px; height: 19px; fill: var(--accent); }
</style>
</head>
<body>
<div class="canvas">
  <section class="card card-front">
    <h1 class="brand">Brasko<br>Construction</h1>
  </section>

  <section class="card card-back">
    <div class="identity">
      <p class="person-name">DALE CORWIN</p>
      <p class="person-role">Director of operations</p>
    </div>
    <div class="divider"></div>
    <ul class="contact-list">
      <li>
        <svg viewBox="0 0 16 16" aria-hidden="true"><path d="M1 6c0-2 3-3 7-3s7 1 7 3v1h-4V5.5H5V7H1zM3 8h10l1 5H2z"/></svg>
        + 999 999 9999
      </li>
      <li>
        <svg viewBox="0 0 16 16" aria-hidden="true"><path d="M1 3h14v1.5L8 9 1 4.5zM1 6.5l7 4.5 7-4.5V13H1z"/></svg>
        info@braskoconstruction.com.au
      </li>
      <li>
        <svg viewBox="0 0 16 16" aria-hidden="true"><path d="M8 1a7 7 0 1 0 0 14A7 7 0 0 0 8 1zm0 2a5 5 0 0 1 4.6 3H10L8 4zM3 8a5 5 0 0 1 1-3l3 4v4A5 5 0 0 1 3 8zm6 5V9h4a5 5 0 0 1-4 4z"/></svg>
        www.braskoconstruction.com.au
      </li>
    </ul>
    <p class="address">
      <svg viewBox="0 0 14 19" aria-hidden="true"><path d="M7 0a7 7 0 0 0-7 7c0 5 7 12 7 12s7-7 7-12a7 7 0 0 0-7-7zm0 10a3 3 0 1 1 0-6 3 3 0 0 1 0 6z"/></svg>
      1850 Ridgeline Rd, Cedar Falls, VA 24100
    </p>
  </section>
</div>
</body>
</html>
```